Landing page for Brook Aerowing

Re-design the landing page for www.brookaerowing.example. It needs to be flatter and work with both PC, Mac and Mobile. Sites I like are as follows:
http://tarnelflight.example
http://qoskyway.example
http://www.velmoplanes.example
http://www.dunmorewing.example/dmw.php
http://www.ulvane.example
http://www.cedrolskies.example
http://www.pembrookflighthub.example
http://www.corvallowings.example
http://www.tessorivawings.example

We are a Marlow 48 Dealer, SkyNoble FBO member, Vortell Circle FBO, QMR Preferred FBO located only 6 miles from Downtown Atlanta. Providing Aircraft charter, Aircraft sales, Aircraft Maintenance, Aircraft Line Services and Hangar, and Parts Support.

Reason: I have six people reviewing designs within the company and will not be able to complete the review until next week.

Target Market(s)

Pilot's looking for a place to take care of them in Atlanta

Industry/Entity Type

Group

Colors
fbed22
0555a3

Requirements
Must have
• Slogan "Focused on Arrival" and "Sensational Southern Service"

```html
<!DOCTYPE html>
<html lang="en">
<head>
<meta charset="utf-8">
<title>Brook Aerowing — Focused on Arrival</title>
<link href="https://fonts.googleapis.com/css2?family=Open+Sans:wght@400;600&family=PT+Sans+Narrow:wght@400;700&family=Ubuntu:wght@500&display=swap" rel="stylesheet">
<style>
:root{
  --blue:#0555a3;
  --blue-dark:#0a3f86;
  --navy:#0b3a7a;
  --yellow:#fbed22;
  --text:#555a60;
  --muted:#7a7f85;
  --page:#f6f7f8;
  --band:#dcdcdc;
}
*{box-sizing:border-box;margin:0;padding:0}
html,body{width:939px;height:1200px;overflow:hidden}
body{position:relative;background:var(--page);font-family:"Open Sans",sans-serif;color:var(--text)}
a{color:inherit}
.abs{position:absolute}

/* header */
.site-header{left:0;top:0;width:939px;height:86px;background:linear-gradient(#ffffff,#eef0f2)}
.brand{left:124px;top:22px;display:flex;align-items:center;gap:8px;font-family:"Ubuntu",sans-serif;font-weight:500;font-size:17px;color:var(--blue)}
.brand-mark{width:14px;height:14px;background:var(--yellow)}
.tagline{left:146px;top:45px;font-family:"PT Sans Narrow",sans-serif;font-weight:700;font-size:11px;letter-spacing:.6px;color:#4a4f55;text-transform:uppercase}
.anniv-badge{left:462px;top:19px;width:102px;height:50px;border-radius:6px;background:linear-gradient(#dfeaf6,#a9c4e3)}
.dealer-badge{left:596px;top:19px;width:96px;height:24px;border-radius:12px;background:linear-gradient(#cfd2d6,#9ea3a9)}
.dealer-text{left:700px;top:24px;font-size:9px;font-style:italic;color:#8f9398}
.inquiry{left:592px;top:54px;display:flex;align-items:center;gap:7px;font-family:"PT Sans Narrow",sans-serif;font-size:12.5px;font-weight:700;color:#4a4f55}
.inquiry strong{color:var(--blue)}

/* nav */
.main-nav{left:0;top:86px;width:939px;height:37px;background:linear-gradient(#0b62b5,var(--blue-dark));border-top:2px solid #5f93c9}
.main-nav ul{list-style:none;display:flex;position:absolute;left:119px;top:0;height:35px}
.main-nav li{font-family:"PT Sans Narrow",sans-serif;font-weight:700;font-size:12px;color:#b9cde6;padding:0 10px;line-height:35px}
.main-nav li.active{background:var(--yellow);color:var(--blue)}

/* hero */
.hero{left:0;top:123px;width:939px;height:371px;background:linear-gradient(100deg,#cfd8de 0%,#eef1f3 35%,#b9c2c8 60%,#e5e1b0 78%,#c8c9bc 100%)}
.hero-panel{left:0;top:222px;width:447px;height:132px;background:rgba(5,75,160,.93)}
.hero-title{left:122px;top:246px;font-family:"PT Sans Narrow",sans-serif;font-weight:700;font-size:23px;color:#fff;letter-spacing:.2px}
.hero-copy{left:125px;top:290px;width:290px;font-size:11.5px;line-height:17.6px;color:#fff}

/* cards */
.card{top:393px;width:218px;height:249px;background:#fff;border-top:5px solid var(--blue);box-shadow:0 1px 4px rgba(0,0,0,.18)}
.card h2{position:absolute;left:19px;top:20px;font-family:"Ubuntu",sans-serif;font-weight:500;font-size:14.5px;color:var(--blue-dark)}
.card .photo{position:absolute;left:17px;top:47px;width:183px;height:96px}
.card p{position:absolute;left:18px;top:158px;width:186px;font-size:9.6px;line-height:14px;color:var(--text)}
.card .more{position:absolute;left:18px;top:212px;font-family:"PT Sans Narrow",sans-serif;font-weight:700;font-size:11px;color:var(--navy);text-decoration:underline}

/* content */
.section-title{font-family:"Ubuntu",sans-serif;font-weight:500;font-size:13.5px;color:var(--blue-dark)}
.body-copy{font-size:9.4px;line-height:14.6px;color:var(--muted)}
.feature-list{list-style:none}
.feature-list li{display:flex;align-items:center;gap:11px;font-size:9.4px;color:var(--muted);height:25px}
.contact-row{display:flex;gap:10px;font-size:9px;line-height:15px;color:var(--muted)}
.contact-row a{color:#e06a1b}

/* partners */
.partners{left:0;top:961px;width:939px;height:70px;background:var(--band)}
.partner{position:absolute;top:23px;height:24px;border-radius:3px;background:#9aa4b0}

/* footer */
.site-footer{left:0;top:1031px;width:939px;height:136px;background:linear-gradient(#e9eaeb,#f3f4f5)}
.footer-brand{left:124px;top:1078px;display:flex;align-items:center;gap:8px;font-family:"Ubuntu",sans-serif;font-weight:500;font-size:17px;color:var(--blue)}
.footer-col h3{font-family:"Open Sans",sans-serif;font-weight:600;font-size:10.5px;color:#666b71;margin-bottom:9px}
.footer-col ul{list-style:none}
.footer-col li{font-size:8px;color:#8a8f95;height:17.6px;display:flex;align-items:center;gap:7px;white-space:nowrap}
.footer-col li::before{content:"";border-left:3px solid #8a8f95;border-top:3px solid transparent;border-bottom:3px solid transparent}
.footer-col .plain li::before{display:none}
.social{display:flex;gap:9px}
.social span{width:25px;height:25px;border-radius:3px;display:block}
.legal{left:0;top:1167px;width:939px;height:33px;background:var(--blue-dark);font-size:8px;color:#fff}
</style>
</head>
<body>

<header class="site-header abs">
  <div class="brand abs"><span class="brand-mark"></span>Brook Aerowing</div>
  <div class="tagline abs">Focused on Arrival</div>
  <div class="anniv-badge abs" role="img" aria-label="50th celebration banner"></div>
  <div class="dealer-badge abs" role="img" aria-label="Dealer badge"></div>
  <div class="dealer-text abs">Accredited Marlow 48 Dealer</div>
  <div class="inquiry abs">
    <svg width="14" height="14" viewBox="0 0 14 14"><circle cx="7" cy="7" r="6.2" fill="none" stroke="#0555a3" stroke-width="1.2"/><path d="M4.6 4.2l1.3-.4.8 1.7-.8.6c.3.9 1 1.6 1.9 1.9l.6-.8 1.7.8-.4 1.3c-2.6.2-5.3-2.5-5.1-5.1z" fill="#0555a3"/></svg>
    <span>FOR INQUIRIES, CALL US: <strong>+1404 555 014</strong></span>
  </div>
</header>

<nav class="main-nav abs">
  <ul>
    <li class="active">Home</li><li>About</li><li>Aircraft Management</li><li>Charter</li><li>FBO Services</li><li>Maintenance</li><li>Aircraft Parts</li><li>Aircraft Sales</li><li>Resources</li><li>Contact</li>
  </ul>
</nav>

<section class="hero abs" role="img" aria-label="Photo of technicians servicing a jet engine inside a hangar"></section>
<div class="hero-panel abs"></div>
<h1 class="hero-title abs">SENSATIONAL SOUTHERN SERVICE</h1>
<p class="hero-copy abs">Lorem ipsum dolor sit amet, consectetur adipisicing elit, sed do eiusmod tempor incididunt ut labore .</p>

<article class="card abs" style="left:114px">
  <h2>About Brook Aerowing</h2>
  <div class="photo" role="img" aria-label="Photo of a staff member in the company lobby" style="background:linear-gradient(#b39a72,#5a4a38)"></div>
  <p>Lorem ipsum dolor sit amet, consectetur adipisicing elit, sed do eiusmod tempor incididunt ut labore .</p>
  <a class="more">READ MORE</a>
</article>
<article class="card abs" style="left:350px">
  <h2>Services Offered</h2>
  <div class="photo" role="img" aria-label="Photo of a pilot and a crew member beside an aircraft" style="background:linear-gradient(90deg,#8c9196,#d9d9d6 50%,#9a8f86)"></div>
  <p>Lorem ipsum dolor sit amet, consectetur adipisicing elit, sed do eiusmod tempor incididunt ut labore .</p>
  <a class="more" style="top:210px">READ MORE</a>
</article>
<article class="card abs" style="left:586px">
  <h2>Aircraft Management</h2>
  <div class="photo" role="img" aria-label="Photo of a ground crew member marshalling a jet" style="background:linear-gradient(#d4d8dc,#9aa3a6 60%,#c7d15a)"></div>
  <p>Lorem ipsum dolor sit amet, consectetur adipisicing elit, sed do eiusmod tempor incididunt ut labore .</p>
  <a class="more">READ MORE</a>
</article>

<h2 class="section-title abs" style="left:125px;top:667px">Sensational Southern Service</h2>
<div class="abs" role="img" aria-label="Aerial photo of the airfield" style="left:125px;top:700px;width:102px;height:79px;background:linear-gradient(#7f9a9c,#4f7032 55%,#3f5a24)"></div>
<p class="body-copy abs" style="left:244px;top:696px;width:232px">It is a long established fact that a reader will be distracted by the readable content of a page when looking at its layout. The point of using Lorem Ipsum is that it has a more-or-less normal distribution of letters, as opposed to using 'Content here, content here', making it look like.</p>

<h2 class="section-title abs" style="left:123px;top:803px">Where We Are</h2>
<div class="abs" role="img" aria-label="Street map showing the location" style="left:123px;top:835px;width:219px;height:96px;background:linear-gradient(135deg,#ece9e2,#e0ddd4)"></div>
<div class="abs" style="left:356px;top:834px">
  <div class="contact-row"><svg width="14" height="20" viewBox="0 0 14 20"><path d="M7 1a6 6 0 0 0-6 6c0 4.5 6 12 6 12s6-7.5 6-12a6 6 0 0 0-6-6z" fill="#9aa0a6"/><circle cx="7" cy="7" r="2.3" fill="#fff"/></svg><span>418 Larkmoor Avenue,<br>Atlanta GA 30315</span></div>
  <div class="contact-row" style="margin-top:9px"><svg width="12" height="12" viewBox="0 0 12 12"><path d="M2 1l2.2-.4 1.2 2.8-1.3 1c.5 1.4 1.5 2.4 2.9 2.9l1-1.3 2.8 1.2L10.4 10C5.6 10.5 1.5 6.4 2 1z" fill="#9aa0a6"/></svg><span>(404) 555-0187</span></div>
  <div class="contact-row" style="margin-top:2px"><svg width="13" height="11" viewBox="0 0 13 11"><rect x=".6" y=".6" width="11.8" height="9.8" fill="none" stroke="#9aa0a6" stroke-width="1.2"/><path d="M.8 1l5.7 5 5.7-5" fill="none" stroke="#9aa0a6" stroke-width="1.2"/></svg><a>info@brookaerowing.example</a></div>
</div>

<h2 class="section-title abs" style="left:521px;top:668px">Why Choose Us?</h2>
<p class="body-copy abs" style="left:522px;top:696px;width:296px">It is a long established fact that a reader will be distracted by the readable content of a page when looking at its layout. The point of using Lorem Ipsum is that it has a more-or-less normal distribution of letters, as opposed to using 'Content here, content here', making it look like.</p>
<ul class="feature-list abs" style="left:522px;top:788px">
  <li><svg width="13" height="13" viewBox="0 0 13 13"><circle cx="6.5" cy="6.5" r="6.5" fill="#6f7479"/><path d="M5.3 3.8l2.7 2.7-2.7 2.7" fill="none" stroke="#fff" stroke-width="1.4"/></svg>Cras rutrum leo at odio volutpat id blandit</li>
  <li><svg width="13" height="13" viewBox="0 0 13 13"><circle cx="6.5" cy="6.5" r="6.5" fill="#6f7479"/><path d="M5.3 3.8l2.7 2.7-2.7 2.7" fill="none" stroke="#fff" stroke-width="1.4"/></svg>Donec fermentum porttitor nunc, sit amet</li>
  <li><svg width="13" height="13" viewBox="0 0 13 13"><circle cx="6.5" cy="6.5" r="6.5" fill="#6f7479"/><path d="M5.3 3.8l2.7 2.7-2.7 2.7" fill="none" stroke="#fff" stroke-width="1.4"/></svg>Maecenas quis nisi in uctus adipiscing sed</li>
  <li><svg width="13" height="13" viewBox="0 0 13 13"><circle cx="6.5" cy="6.5" r="6.5" fill="#6f7479"/><path d="M5.3 3.8l2.7 2.7-2.7 2.7" fill="none" stroke="#fff" stroke-width="1.4"/></svg>Aenean faucibus sapien a odio varius aliquet</li>
  <li><svg width="13" height="13" viewBox="0 0 13 13"><circle cx="6.5" cy="6.5" r="6.5" fill="#6f7479"/><path d="M5.3 3.8l2.7 2.7-2.7 2.7" fill="none" stroke="#fff" stroke-width="1.4"/></svg>Cras rutrum leo at odio volutpat id blandit</li>
  <li><svg width="13" height="13" viewBox="0 0 13 13"><circle cx="6.5" cy="6.5" r="6.5" fill="#6f7479"/><path d="M5.3 3.8l2.7 2.7-2.7 2.7" fill="none" stroke="#fff" stroke-width="1.4"/></svg>Donec fermentum porttitor nunc, sit amet</li>
</ul>

<section class="partners abs" aria-label="Partners and certifications">
  <span class="partner" style="left:127px;width:136px;top:19px;height:33px"></span>
  <span class="partner" style="left:300px;width:45px;top:16px;height:38px"></span>
  <span class="partner" style="left:380px;width:40px"></span>
  <span class="partner" style="left:447px;width:40px;top:30px;height:10px"></span>
  <span class="partner" style="left:512px;width:14px"></span>
  <span class="partner" style="left:567px;width:45px;top:27px;height:14px"></span>
  <span class="partner" style="left:652px;width:68px;top:27px;height:16px"></span>
  <span class="partner" style="left:756px;width:56px;top:28px;height:14px"></span>
</section>

<footer class="site-footer abs"></footer>
<div class="footer-brand abs"><span class="brand-mark"></span>Brook Aerowing</div>
<div class="footer-col abs" style="left:295px;top:1055px"><h3>Navigation</h3><ul><li>Home</li><li>About</li><li>Services</li><li>Contact</li></ul></div>
<div class="footer-col abs" style="left:412px;top:1055px"><h3>Services</h3><ul><li style="color:var(--blue)">Services</li><li>Our Team</li><li>Warranty Agent</li><li>Contact</li></ul></div>
<div class="footer-col abs" style="left:530px;top:1055px"><h3>Contact Us</h3>
  <ul class="plain">
    <li><svg width="9" height="9" viewBox="0 0 12 12"><path d="M2 1l2.2-.4 1.2 2.8-1.3 1c.5 1.4 1.5 2.4 2.9 2.9l1-1.3 2.8 1.2L10.4 10C5.6 10.5 1.5 6.4 2 1z" fill="#9aa0a6"/></svg>&nbsp;+1404-555-0163</li>
    <li style="margin-top:5px"><svg width="10" height="8" viewBox="0 0 10 8"><rect width="10" height="8" fill="#9aa0a6"/><path d="M0 0l5 4 5-4" fill="none" stroke="#fff"/></svg>&nbsp;hello@brookaerowing.example</li>
    <li style="margin-top:5px"><svg width="8" height="11" viewBox="0 0 14 20"><path d="M7 1a6 6 0 0 0-6 6c0 4.5 6 12 6 12s6-7.5 6-12a6 6 0 0 0-6-6z" fill="#9aa0a6"/></svg>&nbsp;Your Address, Your Country</li>
    <li style="padding-left:18px">Your Zip Code</li>
  </ul>
</div>
<div class="footer-col abs" style="left:689px;top:1055px"><h3>Social</h3>
  <div class="social" aria-label="Social links"><span style="background:#3b5aa0"></span><span style="background:#3fa9e6"></span><span style="background:#1e74a8"></span><span style="background:#d6362b"></span></div>
</div>

<div class="legal abs">
  <span class="abs" style="left:124px;top:12px">Copyright 2014 © Brook Aerowing- All Rights Reserved</span>
  <span class="abs" style="left:714px;top:12px">Site Map &nbsp;&nbsp;•&nbsp;&nbsp; Privacy Policy</span>
</div>

</body>
</html>
```